Haventrix Corporate Stationery

Look for design of all new corporate stationery for an existing insurance broking business that is going through a redesign and move from older partners to younger family members. New Logo is attached. Company is Brisbane based.
Colours in the Logo is Hex #43bed8 and website features a lot of hex #17b8d8. Website front page "A plan to protect you" - headline. "Professional and Individual advice to protect your greatest assets" - tagline.

Stationery required: Business Cards, Letter head, Thank-you cards, Birthday cards, Presentation folders, With Compliment slips and a powerpoint template. We also would like to send a card to all customers with the something along of the lines of "something new".

Target Market(s)

Customers of Insurance business looking at superannuation, life and income protection insurance, investment advice and wills

Industry/Entity Type

Insurance Broker

Font styles to use
Other font styles liked:
• same as logo

Requirements
Must have
• The above designs for new stationery for the new business including:
• Business Cards, Letter head, Thank-you cards, Birthday cards, Presentation folders, With Compliment slips and a powerpoint template. We also would like to send a card to all customers with the something along of the lines of "something new".
Nice to have
• It is a new look - long time family business being passed to next generation - big focus on advice for YOU, individual advice etc..

```html
<!DOCTYPE html>
<html lang="en">
<head>
<meta charset="utf-8">
<title>Haventrix Business Card</title>
<link href="https://fonts.googleapis.com/css2?family=Open+Sans:ital,wght@0,400;0,600;1,400&display=swap" rel="stylesheet">
<style>
  :root {
    --backdrop: #2b2b2b;
    --card-white: #ffffff;
    --brand-cyan: #43bed8;
    --brand-grey: #85868a;
    --text-grey: #555659;
    --rule-grey: #cfd0d2;
    --band-line: #9a9b9e;
  }
  * { box-sizing: border-box; margin: 0; padding: 0; }
  html, body {
    width: 1200px;
    height: 987px;
    overflow: hidden;
    background: var(--backdrop);
    font-family: "Open Sans", Arial, sans-serif;
  }
  .card {
    position: absolute;
    left: 293px;
    width: 615px;
    height: 351px;
  }
  .card-front { top: 130px; background: var(--card-white); }
  .card-back { top: 505px; background: var(--brand-grey); }

  .brand {
    position: absolute;
    left: 0;
    width: 325px;
    top: 150px;
    display: flex;
    align-items: center;
    justify-content: center;
    gap: 10px;
  }
  .brand-dot {
    width: 22px;
    height: 22px;
    border-radius: 50%;
    background: var(--brand-cyan);
  }
  .brand-name {
    font-size: 34px;
    font-weight: 600;
    color: var(--brand-cyan);
    letter-spacing: 1px;
    line-height: 1;
  }

  .divider {
    position: absolute;
    left: 325px;
    top: 57px;
    width: 1px;
    height: 241px;
    background: var(--rule-grey);
  }

  .contact {
    position: absolute;
    left: 352px;
    top: 62px;
    color: var(--text-grey);
  }
  .person-name {
    font-size: 21px;
    font-weight: 600;
    color: var(--brand-cyan);
    line-height: 25px;
  }
  .person-role {
    font-size: 16px;
    line-height: 22px;
    color: #7c7d80;
    margin-bottom: 7px;
  }
  .address { font-size: 16px; line-height: 23.5px; margin-bottom: 5px; }
  .contact-list { list-style: none; }
  .contact-list li {
    display: flex;
    align-items: center;
    gap: 8px;
    font-size: 16px;
    line-height: 23.5px;
  }
  .contact-list svg { width: 15px; height: 15px; flex: none; }

  .rule-line {
    position: absolute;
    left: 0; right: 0;
    top: 323px;
    height: 2px;
    background: var(--band-line);
  }
  .cyan-band {
    position: absolute;
    left: 0; right: 0;
    top: 327px;
    height: 24px;
    background: var(--brand-cyan);
  }

  .back-brand {
    position: absolute;
    right: 36px;
    top: 232px;
    display: flex;
    align-items: center;
    gap: 8px;
  }
  .back-brand .brand-dot { background: var(--card-white); width: 18px; height: 18px; }
  .back-brand .brand-name { color: var(--card-white); font-size: 28px; }
  .back-url {
    position: absolute;
    right: 31px;
    top: 313px;
    font-size: 15px;
    font-style: italic;
    color: var(--card-white);
  }
</style>
</head>
<body>
  <section class="card card-front">
    <div class="brand">
      <span class="brand-dot"></span>
      <span class="brand-name">HAVENTRIX</span>
    </div>
    <div class="divider"></div>
    <div class="contact">
      <p class="person-name">LIAM CARTER</p>
      <p class="person-role">CEO/FOUNDER</p>
      <p class="address">4218 Banksia Street<br>Fairview, Oregon 52817</p>
      <ul class="contact-list">
        <li>
          <svg viewBox="0 0 16 16"><path fill="#43bed8" d="M3.5 1.5l2.5 0 1 3.5-1.8 1.3a9 9 0 0 0 4.5 4.5L11 9l3.5 1v2.5c0 1-1 2-2 2C6.5 14.5 1.5 9.5 1.5 3.5c0-1 1-2 2-2z"/></svg>
          555 214 7830
        </li>
        <li>
          <svg viewBox="0 0 16 16"><rect x="4" y="1" width="8" height="14" rx="1.5" fill="none" stroke="#43bed8" stroke-width="1.6"/><circle cx="8" cy="12.3" r="0.9" fill="#43bed8"/></svg>
          555 902 4417
        </li>
        <li>
          <svg viewBox="0 0 16 16"><rect x="4" y="1.5" width="8" height="4" fill="#43bed8"/><rect x="1" y="6" width="14" height="6" rx="1" fill="#43bed8"/><rect x="4" y="10" width="8" height="4.5" fill="#fff" stroke="#43bed8" stroke-width="1.2"/></svg>
          555 368 1295
        </li>
        <li>
          <svg viewBox="0 0 16 16"><rect x="1" y="3.5" width="14" height="9" fill="#43bed8"/><path d="M1.5 4l6.5 5 6.5-5" fill="none" stroke="#fff" stroke-width="1.2"/></svg>
          hello@haventrix.com
        </li>
        <li>
          <svg viewBox="0 0 16 16"><circle cx="8" cy="8" r="7" fill="#43bed8"/><path d="M4 5c2 0 2 2 3.5 2.5S6 11 5 10.5 3.5 7 4 5zM10 3.5c1 1 2.5 1 2.5 3s-1.5 1-2 2-1 3-2 2.5 0-3 .5-4-1-2.5 1-3.5z" fill="#fff"/></svg>
          www.haventrix.com
        </li>
      </ul>
    </div>
    <div class="rule-line"></div>
    <div class="cyan-band"></div>
  </section>

  <section class="card card-back">
    <div class="back-brand">
      <span class="brand-dot"></span>
      <span class="brand-name">HAVENTRIX</span>
    </div>
    <p class="back-url">www.haventrix.com</p>
  </section>
</body>
</html>
```